new roofing company card

New primary business card for roofing company.

Industry/Entity Type

Residential roofing/Specializing in Asphalt and Standing seam metal roofing

Contact Information for Business Card

Phone number is: 484 672 1058 Email: support@fennridgeroofworks.com website: www.fennridgeroofworks.com

Colors
EB3D1F
EC4F4E
F09395
F8D3D4
FCEDEE

```html
<!DOCTYPE html>
<html lang="en">
<head>
<meta charset="utf-8">
<title>Fennridge Roofworks – Business Card</title>
<link rel="stylesheet" href="https://fonts.googleapis.com/css2?family=Libre+Baskerville:wght@400;700&family=Arimo:wght@400&display=swap">
<style>
  :root {
    --stage: #36363a;
    --paper: #f7f7f5;
    --ink: #232222;
    --charcoal: #2a2a2c;
    --charcoal-soft: #3a3a3d;
    --roof-red: #c4231b;
    --muted: #4a4a4a;
    --light: #f2f2f2;
  }
  * { box-sizing: border-box; margin: 0; padding: 0; }
  html, body { width: 1200px; height: 900px; overflow: hidden; }
  body {
    background: var(--stage);
    font-family: "Arimo", Arial, sans-serif;
    position: relative;
  }
  .card {
    position: absolute;
    left: 250px;
    width: 700px;
    height: 400px;
    overflow: hidden;
    box-shadow: 0 10px 28px rgba(0,0,0,.45);
  }
  .card--front { top: 35px; background: var(--paper); }
  .card--back { top: 465px; background: var(--charcoal); }

  .front-shapes { position: absolute; inset: 0; }

  .holder { position: absolute; left: 58px; top: 120px; }
  .holder__name {
    font-family: "Libre Baskerville", Georgia, serif;
    font-weight: 700;
    font-size: 24px;
    color: var(--roof-red);
    letter-spacing: .5px;
    text-transform: uppercase;
  }
  .holder__role { font-size: 17px; color: var(--muted); margin-top: 4px; }

  .brand {
    position: absolute;
    right: 48px;
    top: 60px;
    text-align: center;
    font-family: "Libre Baskerville", Georgia, serif;
    font-weight: 400;
    color: var(--ink);
    line-height: 1.05;
    text-transform: uppercase;
  }
  .brand__main { display: block; font-size: 50px; letter-spacing: 1px; }
  .brand__sub { display: block; font-size: 23px; letter-spacing: 4px; margin-top: 6px; }

  .contact {
    position: absolute;
    left: 150px;
    top: 296px;
    list-style: none;
    color: var(--light);
    font-size: 17px;
  }
  .contact__item { display: flex; align-items: center; gap: 10px; height: 26px; }
  .contact__icon { width: 16px; height: 16px; flex: none; }

  .back-brand {
    position: absolute;
    inset: 0;
    display: flex;
    flex-direction: column;
    align-items: center;
    justify-content: center;
    font-family: "Libre Baskerville", Georgia, serif;
    font-weight: 400;
    color: #4a4a4e;
    text-transform: uppercase;
    line-height: 1.05;
  }
  .back-brand .brand__main { font-size: 62px; }
  .back-brand .brand__sub { font-size: 28px; letter-spacing: 5px; }
</style>
</head>
<body>
  <section class="card card--front">
    <svg class="front-shapes" viewBox="0 0 700 400" width="700" height="400" aria-hidden="true">
      <polygon points="0,298 190,186 445,186 418,206 202,206 0,334" fill="var(--roof-red)"/>
      <polygon points="28,400 212,222 408,222 452,208 700,208 700,400" fill="var(--charcoal)"/>
    </svg>

    <div class="holder">
      <p class="holder__name">Daniel Reyes</p>
      <p class="holder__role">Manager</p>
    </div>

    <p class="brand">
      <span class="brand__main">Fennridge</span>
      <span class="brand__sub">Roofworks</span>
    </p>

    <ul class="contact">
      <li class="contact__item">
        <svg class="contact__icon" viewBox="0 0 16 16" aria-hidden="true"><circle cx="8" cy="8" r="8" fill="var(--roof-red)"/><path d="M5 4.5c.6-.4 1.2 0 1.4.6l.4 1c.2.5-.2.8-.5 1 .4.9 1 1.5 1.9 1.9.2-.3.5-.7 1-.5l1 .4c.6.2 1 .8.6 1.4-.6.9-1.6 1-2.6.5C6.6 10.100 5.4 8.900 4.700 7.300 4.300 6.200 4.300 5.100 5 4.500z" fill="#fff"/></svg>
        <span>484 672 1058</span>
      </li>
      <li class="contact__item">
        <svg class="contact__icon" viewBox="0 0 16 16" aria-hidden="true"><circle cx="8" cy="8" r="8" fill="var(--roof-red)"/><rect x="4" y="5" width="8" height="6" fill="#fff"/><path d="M4 5l4 3.3L12 5" fill="none" stroke="var(--roof-red)" stroke-width="1"/></svg>
        <span>support@fennridgeroofworks.com</span>
      </li>
      <li class="contact__item">
        <svg class="contact__icon" viewBox="0 0 16 16" aria-hidden="true"><circle cx="8" cy="8" r="8" fill="var(--roof-red)"/><circle cx="8" cy="8" r="4.2" fill="none" stroke="#fff" stroke-width="1"/><path d="M3.8 8h8.4M8 3.8c-2 2.400-2 6 0 8.400M8 3.8c2 2.400 2 6 0 8.400" fill="none" stroke="#fff" stroke-width="1"/></svg>
        <span>www.fennridgeroofworks.com</span>
      </li>
    </ul>
  </section>

  <section class="card card--back">
    <p class="back-brand">
      <span class="brand__main">Fennridge</span>
      <span class="brand__sub">Roofworks</span>
    </p>
  </section>
</body>
</html>
```